willowcreekrestoring - healing business promotion

I have and energy / intuitive healing and kinesiology business. working with people who are looking for healing outside of the modern medical model, who have tried but failed in their search for understanding their conditions and why health and or happiness eludes them. the healing is done with love, patience and understanding. I am looking to be taken seriously with my presentation and to reach a person who may be deterred by the thought of angels and intuition! but to not exclude those that are attracted to that also.

Industry/Entity Type

Medical

Contact Information for Business Card

willowcreekrestoring
fast safe deep energy healing system
tamsin louise harte
energy healing / kinesiology and neurotraining
0417266183 07 4158 2746
home visits available for cairns and tablelands
t.lharte@quillmail.com

Requirements
Should not have
• Primary colours

```html
<!DOCTYPE html>
<html lang="en">
<head>
<meta charset="utf-8">
<title>Willow Creek Restoring – Business Card</title>
<link rel="stylesheet" href="https://fonts.googleapis.com/css2?family=EB+Garamond:ital,wght@0,400;0,600;0,700;1,400&family=Great+Vibes&display=swap">
<style>
  :root {
    --card-bg: #ffffff;
    --ink-navy: #23198a;
    --ink-charcoal: #3a3a3a;
    --font-script: "Great Vibes", cursive;
    --font-serif: "EB Garamond", Garamond, serif;
  }
  html, body {
    margin: 0;
    padding: 0;
    overflow: hidden;
    background: var(--card-bg);
  }
  .card {
    position: relative;
    width: 1200px;
    height: 693px;
    background: var(--card-bg);
    overflow: hidden;
    font-family: var(--font-serif);
  }
  .card__line {
    position: absolute;
    left: 0;
    width: 100%;
    margin: 0;
    text-align: center;
    white-space: nowrap;
    line-height: 1;
  }
  .brand-name {
    top: 118px;
    font-family: var(--font-script);
    font-weight: 400;
    font-size: 104px;
    color: var(--ink-navy);
    letter-spacing: 1px;
  }
  .tagline {
    top: 231px;
    font-size: 35px;
    color: var(--ink-charcoal);
    letter-spacing: 3px;
  }
  .practitioner {
    top: 358px;
    font-size: 31px;
    font-weight: 700;
    color: var(--ink-navy);
    letter-spacing: 2px;
  }
  .modalities {
    top: 403px;
    font-size: 30px;
    font-style: italic;
    color: var(--ink-charcoal);
  }
  .phones {
    top: 445px;
    font-size: 32px;
    color: var(--ink-navy);
    letter-spacing: 1.5px;
  }
  .email {
    top: 487px;
    font-size: 31px;
    color: var(--ink-navy);
    letter-spacing: 2px;
  }
  .service-area {
    top: 583px;
    font-size: 25px;
    font-variant: small-caps;
    text-transform: lowercase;
    color: var(--ink-navy);
    letter-spacing: 2.5px;
  }
</style>
</head>
<body>
  <main class="card">
    <h1 class="card__line brand-name">Willow Creek Restoring</h1>
    <p class="card__line tagline">fast, safe, deep, energy healing system</p>
    <p class="card__line practitioner">Tamsin Louise</p>
    <p class="card__line modalities">harte energy healing / kinesiology and neurotraining</p>
    <p class="card__line phones">0417266183 07 4158 2746</p>
    <p class="card__line email">t.lharte@quillmail.com</p>
    <p class="card__line service-area">Home visits available for Cairns and Tablelands</p>
  </main>
</body>
</html>
```